Label design for Japanese healthy drink

We need new label design to give our product a new look. This is Amazake, traditional Japanese drink made out of fermented rice. This is nutrition packed drink and target audience is health conscious people. We want something simple and healthy. The attached photo is current label (for the size reference only) and food pouch the label will be attached. Please don't use anything on the label in the picture.

Target Market(s)

health conscious people (30s - 50s)

Requirements
Must have
• "Amazake"
Should not have
• too much color, picture of rice or sake

```html
<!DOCTYPE html>
<html lang="en">
<head>
<meta charset="utf-8">
<title>Amazake Label</title>
<link rel="stylesheet" href="https://fonts.googleapis.com/css2?family=Bodoni+Moda:wght@400;500&family=Montserrat:ital,wght@0,500;0,600;1,700&family=Pinyon+Script&family=Noto+Sans+JP:wght@700&display=swap">
<style>
  :root {
    --stage-top: #7a8a9b;
    --stage-bottom: #5e7083;
    --label-navy: #231f3a;
    --label-gold: #dca54d;
    --label-white: #ffffff;
    --label-soft: #d9d6df;
  }
  html, body {
    margin: 0;
    padding: 0;
    width: 1200px;
    height: 849px;
    overflow: hidden;
  }
  body {
    background: linear-gradient(160deg, var(--stage-bottom) 0%, var(--stage-top) 100%);
    position: relative;
  }
  .amazake-label {
    position: absolute;
    left: 338px;
    top: 136px;
    width: 523px;
    height: 577px;
  }
  .label-body { fill: var(--label-navy); }
  .label-stripe { fill: var(--label-gold); }
  .oval-outer { fill: var(--label-navy); }
  .oval-ring { fill: var(--label-gold); }
  .oval-inner-line { fill: none; stroke: var(--label-white); stroke-width: 3; }
  .oval-core { fill: var(--label-navy); }
  .origin-line {
    font-family: "Montserrat", sans-serif;
    font-weight: 600;
    font-size: 31px;
    fill: var(--label-white);
    letter-spacing: 1px;
  }
  .kanji-name {
    font-family: "Noto Sans JP", sans-serif;
    font-weight: 700;
    font-size: 44px;
    fill: var(--label-white);
  }
  .product-name {
    font-family: "Bodoni Moda", serif;
    font-weight: 400;
    font-size: 142px;
    fill: var(--label-gold);
  }
  .name-dot { fill: var(--label-gold); }
  .organic-script {
    font-family: "Pinyon Script", cursive;
    font-size: 48px;
    fill: var(--label-soft);
  }
  .descriptor {
    font-family: "Montserrat", sans-serif;
    font-weight: 600;
    font-size: 26px;
    fill: var(--label-white);
  }
  .natural-percent {
    font-family: "Montserrat", sans-serif;
    font-style: italic;
    font-weight: 700;
    font-size: 70px;
    fill: var(--label-white);
  }
  .natural-word {
    font-family: "Montserrat", sans-serif;
    font-weight: 500;
    font-size: 40px;
    fill: var(--label-white);
    letter-spacing: 1px;
  }
  .grain-ornament { fill: var(--label-gold); }
</style>
</head>
<body>
  <svg class="amazake-label" viewBox="285 485 670 740" xmlns="http://www.w3.org/2000/svg">
    <defs>
      <path id="descriptor-arc" d="M357,797 A 262 121 0 0 0 881 797"/>
    </defs>

    <g class="label-panel">
      <rect class="label-body" x="435" y="492" width="368" height="728" rx="42"/>
      <rect class="label-stripe" x="447" y="506" width="10" height="700" rx="3"/>
      <rect class="label-stripe" x="781" y="506" width="10" height="700" rx="3"/>
    </g>

    <g class="origin-block" text-anchor="middle">
      <text class="origin-line" x="619" y="551">MADE IN</text>
      <text class="origin-line" x="619" y="588">JAPAN</text>
    </g>

    <g class="name-oval">
      <ellipse class="oval-outer" cx="619" cy="791" rx="330" ry="182"/>
      <ellipse class="oval-ring" cx="619" cy="791" rx="318" ry="172"/>
      <ellipse class="oval-core" cx="619" cy="785" rx="302" ry="158"/>
      <ellipse class="oval-inner-line" cx="619" cy="784" rx="292" ry="154"/>

      <text class="kanji-name" x="619" y="692" text-anchor="middle">甘酒</text>

      <circle class="name-dot" cx="366" cy="801" r="6"/>
      <circle class="name-dot" cx="873" cy="801" r="6"/>
      <text class="product-name" x="394" y="824" textLength="456" lengthAdjust="spacingAndGlyphs">AMAZAKE</text>

      <text class="organic-script" x="619" y="874" text-anchor="middle">Organic</text>

      <text class="descriptor" text-anchor="middle">
        <textPath href="#descriptor-arc" startOffset="50%">Fermented Japanese Rice Drink</textPath>
      </text>
    </g>

    <g class="natural-claim" text-anchor="middle">
      <text class="natural-percent" x="625" y="1068">100%</text>
      <text class="natural-word" x="628" y="1112">NATURAL</text>
    </g>

    <rect class="grain-ornament" x="530" y="1142" width="176" height="18" rx="9"
          role="img" aria-label="Small gold grain-stalk ornament"/>
  </svg>
</body>
</html>
```